Wine Label Design-Crumbled Ledge Vineyard

Crumbled Ledge Vineyard is in the Barossa Valley in South Australia. The Barossa is recognized as Australia's premier wine region, producing Australia's icon wines and some " new takes on traditional".
This family owned and operated vineyard grows some exceptionally high quality fruit. Most of the fruit is sold and used for some of Australia's most iconic wines. Small quantities are retained by the owners for some wines with very limited availability. (Wines were previously sold as BrellMarston Vineyards Crumbled Ledge ( Shiraz, Cabernet etc).

The wines will in the future be labeled simply ‘Crumbled Ledge Vineyard’. The label will launch this new identity for the single family single vineyard and its high quality wines which are a true expression of the vineyard and derive from the Crumbled Ledge common to this ancient area (800-2000 million years old).
The label should reflect
• Single vineyard, family owned
• vines in very old rock & soils
• High quality & reliability
• Edgy but true, design based thinking (Please note:blue is generally seen as an unacceptable colour for a wine label?? Don’t ask me why)

The wines will be sold mostly direct in Australia ( ie not through retail stores), with limited export to Asia, Scandinavia and Canada.
There are three quality levels and price points in the portfolio
1. Entry level premium for everyday drinking for discriminating drinkers-approx AUD20
2. Super Premium-approx AUD30
3. Limited Release ultlra premium-AUD75-90?
We envisage three variations on the label but with an obvious & common design element. This design element should be able to be used for corporate identification and promotion
The paper stock will be waterproof and self adhesive. Our preference is for designs that engage the user by appealing to both sight and touch. It is preferred that textures be added eg embossing, high build varnish etc-rather than be a facet of the stock itself.
For information on statutory label requirements refer to www.vinoregistry-example.com . In brief
o Front label need not show any mandatory information. However we would prefer Variety, Barossa Valley, Year and alcohol to be shown on the front label
o Back label should show all mandatories and allow for a bar code

Reason: I've had a problem with my wireless broadband account and reception has been intermittent to say the least to the extent that I switched off at the weekend. Just going downtown now for a 'polite discussion' with my service provider.

Reason: I have receiver insufficient designs of quality which we would consider. Too many designs have a "cut and paste" appearance - too few exhibit an original art/design element which truly identifies the product.

Gals & Guys

most of the designs submitted lack punch and originality and are totally unmemorable.
Please-get on Zindle or whatever enter "Wine Label Designs" and do some research b4 u waste your time and mine. Formulaic cut and paste will not win the day. That's not to say that cut and paste can't work-but it must have some originality, impact and command attention. Please surprise me.

Following on from a question from a designer about who is our competition and what we are looking for I sent the following 
"I don't think I can add anything new. Read the brief and comments again and research wine labels on the web. In 30 minutes you'll get a good idea of the creative edgy designs in the industry. There are a plethora of collections. Our competition-anyone with a label. In 2010 there were over 2400 "producers" in other words 2400 producers with at least one label. In fact there are over 25000 Australian wines and then the numerous imported wines.

Target Market(s)

$20 people who budget everyday but have graduated from drinking 'entry level' wines. These people will likely fit into Cat. (b) in the $30 wine

$30 (a) will not over-compromise on some everyday discretionary expenditure.(b) might buy for special occasions

$70-$90 Professional/successful people with high disposable/discretionary income not particularly worried about recession. wine geeks.

Industry/Entity Type

Retail

Requirements
Must have
• identifiable element across range of wines

```html
<!DOCTYPE html>
<html lang="en">
<head>
<meta charset="utf-8">
<title>Crumbled Ledge Vineyard – Wine Label Range</title>
<link rel="stylesheet" href="https://fonts.googleapis.com/css2?family=Pinyon+Script&family=Crimson+Text:wght@400;700&family=Cinzel:wght@700&display=swap">
<style>
  :root {
    --paper: #ffffff;
    --navy: #0d0a55;
    --gold: #e6b84e;
    --tier-premium: #0a3a9c;
    --tier-super: #0b7a0b;
    --tier-ultra: #a80808;
  }
  * { margin: 0; padding: 0; box-sizing: border-box; }
  html, body {
    width: 1200px; height: 900px; overflow: hidden;
    background: var(--paper);
  }
  .range { position: relative; width: 1200px; height: 900px; }

  .label {
    position: absolute;
    width: 391px; height: 346px;
    background: var(--navy);
    border-radius: 21px;
    color: var(--gold);
    font-family: "Crimson Text", Georgia, serif;
    text-align: center;
  }
  .label--premium { left: 187px; top: 84px; --tier: var(--tier-premium); }
  .label--super   { left: 622px; top: 84px; --tier: var(--tier-super); }
  .label--ultra   { left: 405px; top: 469px; --tier: var(--tier-ultra); }

  .label__frame {
    position: absolute; inset: 12px;
    border: 3px solid var(--gold);
    border-radius: 14px;
    overflow: hidden;
  }

  .label__mark {
    position: absolute; left: 0; right: 0; top: 54px;
    display: flex; justify-content: center; align-items: center; gap: 8px;
    font-size: 15px; font-weight: 400; letter-spacing: 0.5px;
  }
  .label__mark-square {
    width: 18px; height: 18px;
    background: var(--tier);
    border: 2px solid var(--gold);
  }

  .label__flourish {
    position: absolute; left: 50%; transform: translateX(-50%);
    width: 250px; height: 1.5px;
    background: linear-gradient(90deg, transparent, var(--gold) 25%, var(--gold) 75%, transparent);
  }
  .label__flourish--top { top: 105px; }
  .label__flourish--bottom { top: 146px; }

  .label__name {
    position: absolute; left: 0; right: 0; top: 104px;
    font-family: "Pinyon Script", cursive;
    font-size: 31px; line-height: 40px;
    white-space: nowrap;
  }
  .label__vintage {
    position: absolute; left: 0; right: 0; top: 155px;
    font-weight: 700; font-size: 17px; line-height: 20px;
  }
  .label__region {
    position: absolute; left: 0; right: 0; top: 176px;
    font-weight: 700; font-size: 13px; line-height: 16px;
  }

  .label__tier {
    position: absolute; left: 0; right: 0; top: 203px; height: 57px;
    background: var(--tier);
    border-top: 3px solid var(--gold);
    border-bottom: 3px solid var(--gold);
    padding-top: 6px;
  }
  .label__tier-name {
    font-family: "Cinzel", "Times New Roman", serif;
    font-weight: 700; font-size: 19px; letter-spacing: 3px;
    line-height: 22px;
  }
  .label__variety { font-size: 13px; line-height: 15px; }

  .label__facts {
    position: absolute; left: 27px; right: 27px; top: 271px;
    display: flex; justify-content: space-between;
    font-size: 13px; line-height: 16px;
    padding-bottom: 4px;
    border-bottom: 1px solid var(--gold);
  }
  .label__address {
    position: absolute; left: 0; right: 0; top: 293px;
    font-size: 8.5px; line-height: 11px;
    white-space: nowrap;
  }
</style>
</head>
<body>
<main class="range">

  <article class="label label--premium">
    <div class="label__frame">
      <div class="label__mark"><span class="label__mark-square"></span><span>Crumbled Ledge</span></div>
      <div class="label__flourish label__flourish--top"></div>
      <h1 class="label__name">Crumbled Ledge Vineyard</h1>
      <div class="label__flourish label__flourish--bottom"></div>
      <p class="label__vintage">2006</p>
      <p class="label__region">Barossa Valley - South Australia</p>
      <div class="label__tier">
        <p class="label__tier-name">PREMIUM</p>
        <p class="label__variety">Cabernet Sauvignon</p>
      </div>
      <div class="label__facts"><span>750 mL</span><span>Standard drinks - 8,3</span><span>13,5% ALC/VOL.</span></div>
      <p class="label__address">Crumbled Ledge Vineyard , Barossa Valley , Elm Lane 14/20, South Australia</p>
    </div>
  </article>

  <article class="label label--super">
    <div class="label__frame">
      <div class="label__mark"><span class="label__mark-square"></span><span>Crumbled Ledge</span></div>
      <div class="label__flourish label__flourish--top"></div>
      <h1 class="label__name">Crumbled Ledge Vineyard</h1>
      <div class="label__flourish label__flourish--bottom"></div>
      <p class="label__vintage">2006</p>
      <p class="label__region">Barossa Valley - South Australia</p>
      <div class="label__tier">
        <p class="label__tier-name">SUPER PREMIUM</p>
        <p class="label__variety">Cabernet Sauvignon</p>
      </div>
      <div class="label__facts"><span>750 mL</span><span>Standard drinks - 8,3</span><span>13,5% ALC/VOL.</span></div>
      <p class="label__address">Crumbled Ledge Vineyard , Barossa Valley , Elm Lane 14/20, South Australia</p>
    </div>
  </article>

  <article class="label label--ultra">
    <div class="label__frame">
      <div class="label__mark"><span class="label__mark-square"></span><span>Crumbled Ledge</span></div>
      <div class="label__flourish label__flourish--top"></div>
      <h1 class="label__name">Crumbled Ledge Vineyard</h1>
      <div class="label__flourish label__flourish--bottom"></div>
      <p class="label__vintage">2006</p>
      <p class="label__region">Barossa Valley - South Australia</p>
      <div class="label__tier">
        <p class="label__tier-name">ULTRA PREMIUM</p>
        <p class="label__variety">Cabernet Sauvignon</p>
      </div>
      <div class="label__facts"><span>750 mL</span><span>Standard drinks - 8,3</span><span>13,5% ALC/VOL.</span></div>
      <p class="label__address">Crumbled Ledge Vineyard , Barossa Valley , Elm Lane 14/20, South Australia</p>
    </div>
  </article>

</main>
</body>
</html>
```